Etiketten für Imkerei mit Spezialisierung auf Bio Lagenhonig
Zielgruppe
wiesentau.at - BioImkerei Lindorf
Kleine Nebenerwerbs Imkerei mit Spezialisierung auf Bio Lagenhonig (nähere Infos sind auf der Website nachzulesen)
Als weitere Produktlinie bieten wir Honig+ / Honig mit Zutaten wie Himbeer, Erdbeer, Haselnuss, Mohn, Ingwer, Thymian, usw an.
Zielgruppe: Personen die offen für die Vielfalt der Natur sind, gesunde und natürliche Lebensmittel lieben und die bereit sind die aufwändige, großteils manuelle, Arbeit entsprechend zu entlohnen.
Gesucht:
ÄNDERUNG: Da die Anforderung für das ausgesetzte Preisgeld offensichtlich zu komplex ist, reduziere ich die Anforderung auf Etiketten für die Produktserie Honig+, Gesamtkonzepte sind nicht erforderlich werden aber gerne angenommen.
ÜRSPRÜNGLICH:
Redesign der aktuellen Honigetiketten
Basisdesign für Lagenhonig und Honig+ das entsprechende Varianten zulässt.
Aufgabenstellung
Ich wünsche mir ein modernes, edles (oder Öko look) Design mit sehr guten Wiedererkennungswert das sich von gängigen Honigetiketten deutlich abhebt.
Das wiesentau Logo soll enthalten sein kann aber bei Bedarf angepasst werden (z.B. monocrome Verison)
Für Lagenhonig werden derzeit 400g und 100g Gläser mit hohem schwarzen DrehFix Decke und,
für Honig+ 250g und 100g mit hohem silbenen DrehFix Deckel verwendet. Beispiele sind im Webshop unter https://hofkorb.at/index.php/wiesentau ersichtilich.
Für das Ablaufdatum ist evtl. ein Feld für manuelle Stempelung vorzusehen.
Bitte die Sichtfeldregelung der EU Verpackungsverordnung einhalten.
Bisherige Etiketten hatten den Anspruch das diese auf guten Laserdruckern ausdruckbar waren - das ist jetzt nicht mehr zwingend notwendig (wäre für Kleinauflagen aber trotzdem vorteilhaft)

```html
<!DOCTYPE html>
<html lang="de">
<head>
<meta charset="utf-8">
<title>wiesentau – honig plus Etiketten</title>
<link rel="stylesheet" href="https://fonts.googleapis.com/css2?family=Lora:wght@600&family=Oswald:wght@200;300&family=Open+Sans:ital,wght@0,300;1,300&display=swap">
<style>
  :root {
    --canvas: #ffffff;
    --paper: #f7f4f1;
    --ink: #5f5a58;
    --accent: #e8a3a0;
    --mandel: #f9c7c6;
    --brombeere: #cbb9c9;
    --haselnuss: #b8c9b5;
    --erdbeere: #f8a6a4;
  }
  * { box-sizing: border-box; margin: 0; padding: 0; }
  html, body {
    width: 1200px; height: 781px; overflow: hidden;
    background: var(--canvas);
  }
  .sheet { position: relative; width: 1200px; height: 781px; }
  .label {
    position: absolute; width: 508px; height: 350px;
    background: var(--paper); overflow: hidden;
  }
  .label--mandel    { left: 73px;  top: 16px;  --tone: var(--mandel); }
  .label--brombeere { left: 623px; top: 16px;  --tone: var(--brombeere); }
  .label--haselnuss { left: 73px;  top: 418px; --tone: var(--haselnuss); }
  .label--erdbeere  { left: 623px; top: 418px; --tone: var(--erdbeere); }

  .brand {
    position: absolute; left: 0; right: 0; top: 14px;
    display: flex; flex-direction: column; align-items: center;
  }
  .brand__dot {
    width: 14px; height: 14px; border-radius: 50%;
    background: var(--ink); margin-bottom: 4px;
  }
  .brand__name {
    font-family: "Lora", serif; font-weight: 600;
    font-size: 19px; line-height: 1; color: #2f2b2a;
  }
  .brand__tagline {
    font-family: "Open Sans", sans-serif; font-weight: 300;
    font-size: 6px; color: #2f2b2a; margin-top: 4px;
  }

  .pattern {
    position: absolute; left: 0; right: 0; top: 86px; bottom: 0;
    background: var(--tone);
  }

  .badge {
    position: absolute; left: 157px; top: 97px; width: 194px; height: 222px;
  }
  .badge svg { position: absolute; inset: 0; }
  .badge__text {
    position: absolute; inset: 0;
    display: flex; flex-direction: column; align-items: center;
    color: var(--ink);
  }
  .badge__honig {
    font-family: "Open Sans", sans-serif; font-weight: 300;
    font-size: 27px; line-height: 1; margin-top: 34px; letter-spacing: .5px;
  }
  .badge__rule {
    width: 150px; height: 1px; background: var(--accent); margin-top: 6px;
  }
  .badge__plus {
    font-family: "Open Sans", sans-serif; font-style: italic; font-weight: 300;
    font-size: 19px; line-height: 1; color: var(--accent); margin-top: 2px;
  }
  .badge__flavour {
    font-family: "Oswald", sans-serif; font-weight: 200;
    font-size: 42px; line-height: 1; margin-top: 30px; letter-spacing: .5px;
    white-space: nowrap;
  }
</style>
</head>
<body>
<main class="sheet">

  <section class="label label--mandel">
    <header class="brand"><span class="brand__dot"></span><span class="brand__name">wiesentau</span><span class="brand__tagline">honig von der wiese</span></header>
    <div class="pattern" role="img" aria-label="Wabenmuster in Rosa mit fliegenden Bienen"></div>
    <div class="badge">
      <svg viewBox="0 0 194 222" aria-hidden="true"><polygon points="48,2 146,2 192,111 146,220 48,220 2,111" fill="var(--paper)" stroke="#ffffff" stroke-width="3"/></svg>
      <div class="badge__text"><span class="badge__honig">honig</span><span class="badge__rule"></span><span class="badge__plus">plus</span><span class="badge__flavour">MANDEL</span></div>
    </div>
  </section>

  <section class="label label--brombeere">
    <header class="brand"><span class="brand__dot"></span><span class="brand__name">wiesentau</span><span class="brand__tagline">honig von der wiese</span></header>
    <div class="pattern" role="img" aria-label="Wabenmuster in Flieder mit fliegenden Bienen"></div>
    <div class="badge">
      <svg viewBox="0 0 194 222" aria-hidden="true"><polygon points="48,2 146,2 192,111 146,220 48,220 2,111" fill="var(--paper)" stroke="#ffffff" stroke-width="3"/></svg>
      <div class="badge__text"><span class="badge__honig">honig</span><span class="badge__rule"></span><span class="badge__plus">plus</span><span class="badge__flavour">BROMBEERE</span></div>
    </div>
  </section>

  <section class="label label--haselnuss">
    <header class="brand"><span class="brand__dot"></span><span class="brand__name">wiesentau</span><span class="brand__tagline">honig von der wiese</span></header>
    <div class="pattern" role="img" aria-label="Wabenmuster in Salbeigrün mit fliegenden Bienen"></div>
    <div class="badge">
      <svg viewBox="0 0 194 222" aria-hidden="true"><polygon points="48,2 146,2 192,111 146,220 48,220 2,111" fill="var(--paper)" stroke="#ffffff" stroke-width="3"/></svg>
      <div class="badge__text"><span class="badge__honig">honig</span><span class="badge__rule"></span><span class="badge__plus">plus</span><span class="badge__flavour">HASELNUSS</span></div>
    </div>
  </section>

  <section class="label label--erdbeere">
    <header class="brand"><span class="brand__dot"></span><span class="brand__name">wiesentau</span><span class="brand__tagline">honig von der wiese</span></header>
    <div class="pattern" role="img" aria-label="Wabenmuster in Erdbeerrot mit fliegenden Bienen"></div>
    <div class="badge">
      <svg viewBox="0 0 194 222" aria-hidden="true"><polygon points="48,2 146,2 192,111 146,220 48,220 2,111" fill="var(--paper)" stroke="#ffffff" stroke-width="3"/></svg>
      <div class="badge__text"><span class="badge__honig">honig</span><span class="badge__rule"></span><span class="badge__plus">plus</span><span class="badge__flavour">ERDBEERE</span></div>
    </div>
  </section>

</main>
</body>
</html>
```